Book Cover design Paws & Petals Book Cover

Please see attached brief Book title BRAVE BESIDE TAILS AND TIDES
THE QUIET GIFT OF CANINES IN LIVING AND HEALING (INCLUSIVE OF THERAPY, EDUCATION, PARENTING, CARE) I have attached a word document describing the brief. Essentially book cover should include a dog and a person, perhaps an older person and a child, and a dog, emotionally charged faces, no cartoons, happy with designer to play with concept and ideas, please avoid AI looking images.

Target Market(s)

Parents, therapists, teachers, people who work with patients/vulnerable people

Industry/Entity Type

Therapeutic care, education, non fiction

Font styles to use
Sans Serif

Requirements
Must have
• Warmth, emotion. I have included the Author photo and paragraph for the back, and also the spec in the details.

```html
<!DOCTYPE html>
<html lang="en">
<head>
<meta charset="utf-8">
<title>Brave Beside Tails and Tides — Book Cover</title>
<link rel="stylesheet" href="https://fonts.googleapis.com/css2?family=Barlow:wght@400;500;600&family=Cinzel:wght@400&display=swap">
<style>
  :root {
    --page-bg: #ffffff;
    --teal-deep: #3a5757;
    --teal-mid: #4f8580;
    --mist: #9bb8aa;
    --dusk: #cdbba0;
    --ember: #e98a52;
    --flame: #dc4f28;
    --ground: #1d1a20;
    --silhouette: #1e1b22;
    --lime: #a8d472;
    --leaf: #78c36c;
    --coral: #f0686f;
    --rose: #ec6fae;
    --white: #ffffff;
    --spine-line: #6f7676;
  }
  * { margin: 0; padding: 0; box-sizing: border-box; }
  html, body {
    width: 1200px; height: 1200px; overflow: hidden;
    background: var(--page-bg);
  }
  .book-cover {
    position: absolute;
    left: 249px; top: 71px;
    width: 711px; height: 1064px;
    overflow: hidden;
    font-family: "Barlow", sans-serif;
    color: var(--white);
  }
  .cover-photo {
    position: absolute; inset: 0;
    background: linear-gradient(to bottom,
      var(--teal-deep) 0%,
      var(--teal-deep) 36%,
      var(--teal-mid) 47%,
      var(--mist) 60%,
      var(--dusk) 71%,
      var(--ember) 78%,
      var(--flame) 82%,
      var(--ground) 85.5%,
      var(--ground) 100%);
  }
  .photo-subjects {
    position: absolute; inset: 0;
    width: 100%; height: 100%;
  }
  .spine-line {
    position: absolute; left: 16px; top: 4px; bottom: 0;
    width: 3px; background: var(--spine-line);
  }
  .author {
    position: absolute; top: 36px; left: 0; right: 0;
    text-align: center;
    font-family: "Cinzel", serif;
    font-size: 22px; letter-spacing: 3px; line-height: 1;
  }
  .title { position: absolute; left: 0; right: 0; text-align: center; line-height: 1; font-weight: 500; }
  .title-main {
    top: 74px; font-size: 172px; color: var(--lime); letter-spacing: 1px;
  }
  .title-line { font-size: 80px; letter-spacing: 1px; }
  .title-line-two { top: 232px; }
  .title-line-three { top: 304px; }
  .word-leaf { color: var(--leaf); }
  .word-coral { color: var(--coral); }
  .word-white { color: var(--white); }
  .word-rose { color: var(--rose); }
  .subtitle {
    position: absolute; left: 0; right: 0; top: 942px;
    text-align: center;
    font-size: 27px; letter-spacing: 2.5px; line-height: 40px;
    font-weight: 400;
  }
  .subtitle strong { color: var(--lime); font-weight: 600; }
</style>
</head>
<body>
  <div class="book-cover">
    <div class="cover-photo" role="img" aria-label="Photograph: silhouette of a person holding up a stick on the right and a shaggy dog leaping towards it on the left, against a teal sky fading to an orange sunset over tall grass">
      <svg class="photo-subjects" viewBox="0 0 711 1064" preserveAspectRatio="none" aria-hidden="true">
        <defs>
          <filter id="soft-blur" x="-50%" y="-50%" width="200%" height="200%">
            <feGaussianBlur stdDeviation="28"/>
          </filter>
          <linearGradient id="grass-fade" x1="0" y1="0" x2="0" y2="1">
            <stop offset="0" stop-color="#1e1b22" stop-opacity="0"/>
            <stop offset="1" stop-color="#1e1b22" stop-opacity="1"/>
          </linearGradient>
        </defs>
        <g fill="var(--silhouette)" filter="url(#soft-blur)" opacity="0.72">
          <ellipse cx="190" cy="720" rx="120" ry="170"/>
          <ellipse cx="565" cy="660" rx="85" ry="250"/>
        </g>
        <rect x="0" y="840" width="711" height="70" fill="url(#grass-fade)"/>
      </svg>
    </div>
    <div class="spine-line"></div>
    <p class="author">DR HELENA MARSH</p>
    <h1>
      <span class="title title-main">BRAVE</span>
      <span class="title title-line title-line-two"><span class="word-leaf">BESIDE</span> <span class="word-coral">TAILS</span></span>
      <span class="title title-line title-line-three"><span class="word-white">AND</span> <span class="word-rose">TIDES</span></span>
    </h1>
    <p class="subtitle">THE QUIET <strong>GIFT OF CANINES</strong><br>IN LIVING AND HEALING</p>
  </div>
</body>
</html>
```